■成果物
新聞広告(カラー突き出し)天地9.8cm×左右6.3cm
・イラストレーターCS4以下でご制作いただきフォントはアウトライン化を施してください。
PDFも一緒に添付していただきますようお願いいたします

■目的
FPによる保険相談のお申込み

■ターゲット
教師・先生

■スケジュール
提案締切:10/12(土)
入稿:10/18(金)
構成案は添付ファイル参照
※キャッチ変え4パターンですが、提案は1パターンでOKです。
ご担当が確定次第、残3パターンを展開いただく予定です。
暖色系
• 高解像度JPG (.jpg)
• イラストレーター形式 (.ai)
専門新聞1面での出稿ですが、スペースが小さいので、とにかく目立たせたいです。
本屋のPOPのような強いビジュアルをイメージしております。
ロゴ素材を添付いたします。

小スペースでのインパクトが最も強かったため

このたびは、多数のご提案ありがとうございました。
残念ながら、採用できなかった方も良い案で迷いました。

引続き、依頼させていただくことがあろうかと思いますが、
今後ともよろしくお願いいたします。

```html
<!DOCTYPE html>
<html lang="ja">
<head>
<meta charset="utf-8">
<title>どうする？家計! 保険えらびかた相談</title>
<link rel="stylesheet" href="https://fonts.googleapis.com/css2?family=Noto+Sans+JP:wght@400;700;900&display=swap">
<style>
  :root {
    --ad-yellow: #ffef1a;
    --ink: #111111;
    --accent-red: #e60012;
    --accent-orange: #f08300;
    --paper: #ffffff;
    --rule: #444444;
    --button-grey: #e8e8e8;
  }
  html, body { margin: 0; padding: 0; overflow: hidden; }
  body { width: 814px; height: 1200px; background: var(--paper); }
  .ad {
    position: relative; width: 814px; height: 1200px; overflow: hidden;
    background: var(--ad-yellow);
    font-family: "Noto Sans JP", sans-serif; color: var(--ink);
  }
  .headline-question {
    position: absolute; left: 30px; top: 18px; margin: 0;
    font-size: 128px; font-weight: 900; line-height: 1; letter-spacing: -4px;
  }
  .headline-main {
    position: absolute; left: 36px; top: 190px; margin: 0;
    font-size: 250px; font-weight: 900; line-height: 1; letter-spacing: -8px;
  }
  .service-tag {
    position: absolute; left: 712px; top: 100px;
    writing-mode: vertical-rl; font-size: 34px; font-weight: 700;
    line-height: 1; letter-spacing: 2px;
  }
  .service-tag .hi { color: var(--accent-red); }
  .service-tag .mid { color: var(--accent-orange); }
  .body-copy {
    position: absolute; left: 40px; top: 500px; margin: 0;
    font-size: 37px; font-weight: 900; line-height: 48px; white-space: nowrap;
  }
  .stamp {
    position: absolute; left: 684px; top: 644px; width: 114px; height: 104px;
    background: var(--accent-red); border: 4px solid var(--paper);
    border-radius: 10px; box-shadow: 0 0 0 3px var(--accent-red);
    transform: rotate(-4deg); box-sizing: border-box;
    color: var(--paper); font-weight: 900; font-size: 38px; line-height: 44px;
    text-align: center; display: flex; flex-direction: column; justify-content: center;
  }
  .offer-lead {
    position: absolute; left: 40px; top: 702px; margin: 0;
    color: var(--accent-red); font-size: 42px; font-weight: 900; line-height: 60px; white-space: nowrap;
  }
  .offer-prize {
    position: absolute; left: 40px; top: 770px; margin: 0;
    color: var(--accent-red); font-weight: 900; white-space: nowrap; line-height: 80px;
  }
  .offer-prize .label { font-size: 34px; }
  .offer-prize .amount { font-size: 80px; letter-spacing: -2px; margin-left: 8px; }
  .offer-prize .unit { font-size: 34px; }
  .offer-prize .gift { font-size: 34px; margin-left: 4px; }
  .terms-target {
    position: absolute; right: 40px; top: 774px; margin: 0;
    text-align: right; font-size: 17px; line-height: 24px; font-weight: 400;
  }
  .terms {
    position: absolute; left: 40px; right: 40px; top: 856px; margin: 0;
    font-size: 17px; line-height: 24px; font-weight: 400; text-align: justify;
  }
  .contact-bar {
    position: absolute; left: 0; right: 0; top: 965px; bottom: 0;
    background: var(--paper); border-top: 3px solid var(--rule);
  }
  .brand {
    position: absolute; left: 30px; top: 34px; display: flex; align-items: center; gap: 14px;
    font-size: 46px; font-weight: 700; white-space: nowrap;
  }
  .brand-dot { width: 48px; height: 48px; border-radius: 50%; background: var(--accent-red); }
  .phone {
    position: absolute; left: 30px; top: 118px; display: flex; align-items: center; gap: 8px;
    font-size: 46px; font-weight: 900; line-height: 60px; white-space: nowrap;
  }
  .search {
    position: absolute; right: 30px; top: 34px; display: flex; height: 64px;
    border: 3px solid var(--rule); font-size: 30px; font-weight: 700;
  }
  .search .field { padding: 0 18px; display: flex; align-items: center; background: var(--paper); }
  .search .button {
    padding: 0 16px; display: flex; align-items: center;
    background: var(--button-grey); border-left: 3px solid var(--rule);
  }
  .url {
    position: absolute; right: 30px; top: 132px; font-size: 24px; font-weight: 700; white-space: nowrap;
  }
</style>
</head>
<body>
<main class="ad">
  <h1 class="headline-question">どうする？</h1>
  <p class="headline-main">家計!</p>
  <div class="service-tag">保険<span class="hi">え</span><span class="mid">ら</span><span class="hi">び</span><span class="mid">か</span><span class="hi">た</span>相談</div>

  <p class="body-copy">増税、年金不安、出費は減らず…。<br>センセイだって、家計が心配な今日この頃。<br>そこで保険相談。保険料を節約し、保険で<br>おカネを貯める方、プロが教えます。</p>

  <div class="stamp"><span>出張</span><span>無料</span></div>

  <p class="offer-lead">今なら、ご相談された方全員に</p>
  <p class="offer-prize"><span class="label">商品券</span><span class="amount">5000</span><span class="unit">円</span><span class="gift">プレゼント!</span></p>
  <p class="terms-target">サービス対象<br>年齢20-70歳、受付時に</p>
  <p class="terms">登録した個人情報は、商品券発送に利用します。商品券は、相談後2ヶ月をめどに、保険のひろば株式会社から発送されます。職業、健康状態、申告内容、相談に必要な情報提供の可否により、サービスを提供できない場合があります。詳細はホームページ利用規約をご覧ください。</p>

  <footer class="contact-bar">
    <div class="brand"><span class="brand-dot"></span><span>保険のひろば</span></div>
    <div class="phone">
      <svg width="44" height="44" viewBox="0 0 24 24" aria-hidden="true"><path fill="#111" d="M6.6 10.8c1.4 2.8 3.8 5.1 6.6 6.6l2.2-2.2c.3-.3.7-.4 1-.2 1.1.4 2.3.6 3.6.6.6 0 1 .4 1 1V20c0 .6-.4 1-1 1C10.6 21 3 13.4 3 4c0-.6.4-1 1-1h3.5c.6 0 1 .4 1 1 0 1.3.2 2.5.6 3.6.1.3 0 .7-.2 1z"/></svg>
      <span>0120-000-000</span>
    </div>
    <div class="search"><span class="field">保険のひろば</span><span class="button">検索</span></div>
    <div class="url">www.hoken-hiroba.example</div>
  </footer>
</main>
</body>
</html>
```